Company Web Design Project

Vantor grids works in the market of renewable energy with energy monitoring systems.

Vantor-grid wants a light and easy company website that informs about our core business and our products as well as the company. The sites should work on multiple platforms. It should include pictures and possibilities for news.
You find elements and company information on the following links:

http://vantor-grid.example/english-version/index.htm
some productinformation you find on this site:
http://kelwatch.example/

Vantor-grid AG is also interested in a Powerpoint template that matches the new website design as well as businesscards and a letter template.

Some more information about the company.

Headquartered in Karlsruhe, Germany, Vantor-Grid AG manufactures hardware & software solutions for remote monitoring, analysis, and control of electrical installations, alarm systems, and other critical networks.

In addition, our company provides test, measurement, and control equipment for use in a wide range of industrial and biological processes.

Founded in the year 2000, Vantor-Grid AG has established a comprehensive service network. Our solutions and systems are in operation e.g. in Europe, USA, Brazil, and Asia.

Vantor-Grid's team of experienced engineers, physicists, and network specialists continuously develop innovative solutions for many key industries - particularly in the renewable energies field.

To ensure the operational safety of their plants by means of optimized real time fault analysis routines

for process optimization

for a measurable increase in yield from production and trade.

Our products are distributed globally via an international dealer network.

In the interest of our customers and their needs, our aim is to expand this dealer network even more.
Updates

Target Market(s)

large solar project companies like, large renewable energy investors, large wholesellers for renewable energy, producer of solar panels.

Industry/Entity Type

Electrical

Requirements
Must have
• responsive design for multiple platforms

```html
<!DOCTYPE html>
<html lang="en">
<head>
<meta charset="utf-8">
<title>Vantor grids – Home</title>
<link rel="stylesheet" href="https://fonts.googleapis.com/css2?family=Quicksand:wght@300;400;600;700&family=Open+Sans:wght@400;600;700&display=swap">
<style>
  :root {
    --green: #1a8570;
    --green-dark: #0f6b58;
    --nav-grey: #7a7a7a;
    --nav-grey-dark: #5e5e5e;
    --ink: #1d1d1d;
    --text-grey: #8a8a8a;
    --footer: #4a463f;
    --footer-text: #e8e6e2;
    --white: #ffffff;
    --grass-light: #5c9a3a;
    --grass-dark: #1f4d18;
  }
  * { margin: 0; padding: 0; box-sizing: border-box; }
  html, body { width: 1117px; height: 1200px; overflow: hidden; background: var(--white); }
  body { position: relative; font-family: "Open Sans", Arial, sans-serif; color: var(--ink); }

  .site-header { position: absolute; left: 0; top: 0; width: 1117px; height: 123px; background: var(--white); }
  .brand { position: absolute; left: 109px; top: 40px; display: flex; align-items: center; gap: 10px; }
  .brand-mark { width: 30px; height: 30px; background: var(--green-dark); }
  .brand-name { font-family: "Quicksand", sans-serif; font-weight: 700; font-size: 28px; color: var(--ink); letter-spacing: -0.5px; }

  .main-nav { position: absolute; left: 393px; top: 49px; height: 30px; display: flex; box-shadow: 0 1px 2px rgba(0,0,0,.25); }
  .main-nav a { display: flex; align-items: center; justify-content: center; height: 30px; font-family: "Quicksand", sans-serif; font-weight: 700; font-size: 11px; color: var(--white); text-decoration: none; background: linear-gradient(var(--nav-grey), var(--nav-grey-dark)); border-right: 1px solid #9a9a9a; }
  .main-nav a:last-child { border-right: none; }
  .main-nav a.is-active { background: var(--green); }

  .hero { position: absolute; left: 0; top: 123px; width: 1117px; height: 551px; }
  .hero-photo { position: absolute; inset: 0; background: radial-gradient(ellipse at 60% 50%, var(--grass-light), var(--grass-dark) 80%); }
  .hero-title { position: absolute; left: 112px; top: 163px; font-family: "Quicksand", sans-serif; font-weight: 300; font-size: 45px; color: var(--white); line-height: 1; }
  .hero-title strong { font-weight: 700; }
  .hero-lead { position: absolute; left: 112px; top: 226px; width: 560px; font-family: "Quicksand", sans-serif; font-weight: 400; font-size: 28px; line-height: 35px; color: var(--white); }
  .hero-arrow { position: absolute; top: 384px; width: 20px; height: 30px; }
  .hero-arrow.prev { left: 89px; }
  .hero-arrow.next { left: 1014px; }

  .features { position: absolute; left: 0; top: 674px; width: 1117px; height: 466px; background: linear-gradient(#f1f1f1, #ffffff 14%, #ffffff 86%, #f0f0f0); }
  .feature { position: absolute; top: 35px; width: 170px; text-align: center; }
  .feature-icon { width: 47px; height: 47px; margin: 0 auto; border-radius: 8px; background: linear-gradient(#ffffff, #d9d9d9); box-shadow: 0 1px 3px rgba(0,0,0,.3); display: flex; align-items: center; justify-content: center; }
  .feature-title { margin-top: 17px; font-family: "Quicksand", sans-serif; font-weight: 400; font-size: 19px; color: var(--ink); }
  .feature-title.is-highlight { color: var(--green); font-weight: 700; }
  .feature-text { margin-top: 10px; font-size: 10.5px; line-height: 14.5px; color: var(--text-grey); }

  .welcome { position: absolute; left: 149px; top: 922px; width: 500px; }
  .section-title { font-family: "Quicksand", sans-serif; font-weight: 400; font-size: 22px; color: var(--ink); }
  .section-title strong { font-weight: 700; }
  .welcome p { margin-top: 14px; font-size: 10.3px; line-height: 14.5px; color: var(--text-grey); }

  .divider { position: absolute; left: 689px; top: 916px; width: 2px; height: 175px; background: linear-gradient(transparent, #cfcfcf 20%, #cfcfcf 80%, transparent); }

  .news { position: absolute; left: 722px; top: 922px; width: 262px; }
  .news-item { margin-top: 12px; }
  .news-item + .news-item { margin-top: 16px; }
  .news-date { font-weight: 700; font-size: 13px; color: var(--green-dark); }
  .news-text { margin-top: 3px; font-size: 10.3px; line-height: 14.5px; color: var(--text-grey); width: 245px; }
  .news-more { display: block; text-align: right; margin-top: -2px; font-weight: 700; font-size: 10.5px; color: var(--green-dark); text-decoration: none; }

  .site-footer { position: absolute; left: 0; top: 1140px; width: 1117px; height: 60px; background: var(--footer); }
  .footer-name { position: absolute; left: 148px; top: 17px; font-family: "Quicksand", sans-serif; font-size: 14px; color: var(--footer-text); }
  .footer-copy { position: absolute; left: 148px; top: 39px; font-size: 6px; color: #a9a49b; }
  .footer-social { position: absolute; left: 812px; top: 16px; display: flex; gap: 20px; }
  .footer-social span { width: 28px; height: 28px; border-radius: 50%; background: #8c877e; }
</style>
</head>
<body>
  <header class="site-header">
    <div class="brand"><span class="brand-mark"></span><span class="brand-name">Vantor-grid</span></div>
    <nav class="main-nav">
      <a class="is-active" href="#" style="width:76px">HOME</a>
      <a href="#" style="width:95px">ABOUT US</a>
      <a href="#" style="width:132px">BUSINESS AREA</a>
      <a href="#" style="width:111px">PRODUCTS</a>
      <a href="#" style="width:93px">TOPICAL</a>
      <a href="#" style="width:107px">CONTACT US</a>
    </nav>
  </header>

  <section class="hero">
    <div class="hero-photo" role="img" aria-label="Photo of a white power socket set into green grass with a black cable plugged in"></div>
    <h1 class="hero-title"><strong>Lorem ipsum</strong> is dummy text</h1>
    <p class="hero-lead">Lorem ipsum dolor sit amet consectetur adispi scing elit. Sed rhonous faucibus.</p>
    <svg class="hero-arrow prev" viewBox="0 0 20 30"><path d="M16 2 L4 15 L16 28" fill="none" stroke="#fff" stroke-width="3"/></svg>
    <svg class="hero-arrow next" viewBox="0 0 20 30"><path d="M4 2 L16 15 L4 28" fill="none" stroke="#fff" stroke-width="3"/></svg>
  </section>

  <section class="features">
    <div class="feature" style="left:132px">
      <div class="feature-icon"><svg width="30" height="30" viewBox="0 0 30 30"><circle cx="15" cy="15" r="12" fill="#3f9b2f"/><g fill="none" stroke="#fff" stroke-width="1.4"><ellipse cx="15" cy="15" rx="5.5" ry="12"/><line x1="3" y1="15" x2="27" y2="15"/><path d="M5 9 H25 M5 21 H25"/></g></svg></div>
      <h2 class="feature-title">Our Solutions</h2>
      <p class="feature-text">Lorem ipsum dolor sit amet consectetur adispiscing elit. Sed rhonous faucibus faucibus maecenas erat odio. Lorem ipsum dolor sit amet.</p>
    </div>
    <div class="feature" style="left:356px">
      <div class="feature-icon"><svg width="32" height="30" viewBox="0 0 32 30"><path d="M3 16 C8 4 24 4 29 14 C24 26 8 26 3 16 Z" fill="#4aa23a"/><path d="M5 16 C13 14 20 14 28 14" stroke="#d6efcf" stroke-width="1.4" fill="none"/></svg></div>
      <h2 class="feature-title">Know the team</h2>
      <p class="feature-text">Lorem ipsum dolor sit amet consectetur adispiscing elit. Sed rhonous faucibus faucibus maecenas erat odio. Lorem ipsum dolor sit amet.</p>
    </div>
    <div class="feature" style="left:594px">
      <div class="feature-icon"><svg width="30" height="30" viewBox="0 0 30 30"><circle cx="15" cy="15" r="13" fill="#3f9b2f"/><path d="M21 11 A7 7 0 1 0 22 16" fill="none" stroke="#fff" stroke-width="2.5"/><path d="M23 6 L23 12 L17 12 Z" fill="#fff"/></svg></div>
      <h2 class="feature-title is-highlight">About us</h2>
      <p class="feature-text">Lorem ipsum dolor sit amet consectetur adispiscing elit. Sed rhonous faucibus faucibus maecenas erat odio. Lorem ipsum dolor sit amet.</p>
    </div>
    <div class="feature" style="left:821px">
      <div class="feature-icon"><svg width="26" height="32" viewBox="0 0 26 32"><path d="M13 2 C8 11 4 16 4 21 A9 9 0 0 0 22 21 C22 16 18 11 13 2 Z" fill="#3f9b2f"/><path d="M8 22 A5 5 0 0 0 13 27" stroke="#d6efcf" stroke-width="1.6" fill="none"/></svg></div>
      <h2 class="feature-title">Our guarantee</h2>
      <p class="feature-text">Lorem ipsum dolor sit amet consectetur adispiscing elit. Sed rhonous faucibus faucibus maecenas erat odio. Lorem ipsum dolor sit amet.</p>
    </div>
  </section>

  <section class="welcome">
    <h2 class="section-title">Welcome To <strong>Vantor grids</strong></h2>
    <p>Lorem ipsum dolor sit amet, consectetur adipiscing elit. Sed rhoncus faucibus faucibus. Maecenas erat odio, mattis id suscipit a, ullamcorper nec felis. Pellentesque ut sem et ante condimentum ultrices quis nec lorem. Integer non sem justo. Praesent malesuada, nulla id elementum aliquam, elit erat tincidunt justo, ut posuere erat metus eu turpis. Pellentesque habitant morbi tristique senectus et netus et malesuada fames ac turpis egestas.</p>
    <p style="margin-top:14px">Donec tempus congue sem, sed volutpat justo mollis semper. Phasellus facilisis, dui sed elementum pretium, metus sapien scelerisque orci, ut accumsan nisi dui at felis.</p>
  </section>

  <div class="divider"></div>

  <section class="news">
    <h2 class="section-title">Latest News</h2>
    <article class="news-item">
      <div class="news-date">February 2013</div>
      <p class="news-text">Lorem ipsum dolor sep sit amet sed lorem ipsum onectur ais piscing eli...</p>
      <a class="news-more" href="#">Read More...</a>
    </article>
    <article class="news-item">
      <div class="news-date">February 2013</div>
      <p class="news-text">Lorem ipsum dolor sep sit amet sed lorem ipsum onectur ais piscing eli...</p>
      <a class="news-more" href="#">Read More...</a>
    </article>
  </section>

  <footer class="site-footer">
    <div class="footer-name">Vantor grids</div>
    <div class="footer-copy">2013 All Rights Reserved</div>
    <div class="footer-social"><span></span><span></span><span></span><span></span></div>
  </footer>
</body>
</html>
```